Business Cards for a law firm

Business cards for our law firm. Use our silhoette logo and OAK HARBOR - check our website (www.oakharbor-legal.com)

Contact Information for Business Card

our silhouette logo, OAK HARBOR, 800-555-0147, Dorian Kestrup, dorian@oakharbor-legal.com

Requirements
Must have
• our silhouette logo, OAK HARBOR, 800-555-0147, Dorian Kestrup, dorian@oakharbor-legal.com

```html
<!DOCTYPE html>
<html lang="en">
<head>
<meta charset="utf-8">
<title>Oak Harbor — Business Cards</title>
<link rel="stylesheet" href="https://fonts.googleapis.com/css2?family=Montserrat:wght@400;700&display=swap">
<style>
  :root {
    --navy: #1b3170;
    --white: #ffffff;
    --ink: #1f2440;
    --backdrop: #e6e7ea;
    --card-shadow: rgba(20, 24, 40, 0.18);
  }
  * { box-sizing: border-box; margin: 0; padding: 0; }
  html, body {
    width: 1200px;
    height: 1200px;
    overflow: hidden;
    background: var(--backdrop);
    font-family: "Montserrat", sans-serif;
  }
  .sheet {
    position: relative;
    width: 1200px;
    height: 1200px;
  }
  .card {
    position: absolute;
    left: 220px;
    width: 760px;
    height: 434px;
    border-radius: 30px;
    box-shadow: 0 10px 30px var(--card-shadow);
    overflow: hidden;
  }
  .card--front { top: 120px; background: var(--white); }
  .card--back  { top: 646px; background: var(--navy); }

  /* front */
  .front-brand {
    position: absolute;
    top: 62px;
    left: 400px;
    display: flex;
    align-items: center;
    gap: 14px;
    color: var(--navy);
    font-weight: 400;
    font-size: 34px;
    letter-spacing: 1px;
  }
  .brand-mark {
    width: 22px;
    height: 22px;
    background: currentColor;
  }
  .divider {
    position: absolute;
    height: 1.5px;
    background: var(--navy);
  }
  .divider--long { top: 226px; left: 372px; width: 330px; }
  .divider--short { top: 268px; left: 70px; width: 300px; }
  .holder-name {
    position: absolute;
    top: 226px;
    left: 70px;
    color: var(--navy);
    font-weight: 700;
    font-size: 25px;
    letter-spacing: 1px;
  }
  .contact-list {
    position: absolute;
    top: 286px;
    left: 70px;
    list-style: none;
    display: flex;
    flex-direction: column;
    gap: 12px;
  }
  .contact-item {
    display: flex;
    align-items: center;
    gap: 14px;
    color: var(--ink);
    font-size: 19px;
  }
  .contact-icon { width: 22px; height: 22px; color: var(--navy); flex: none; }

  /* back */
  .back-brand {
    position: absolute;
    inset: 0;
    display: flex;
    align-items: center;
    justify-content: center;
    gap: 22px;
    color: var(--white);
    font-weight: 400;
    font-size: 62px;
    letter-spacing: 2px;
  }
  .back-brand .brand-mark { width: 36px; height: 36px; }
</style>
</head>
<body>
<main class="sheet">
  <section class="card card--front" aria-label="Business card front">
    <div class="front-brand"><span class="brand-mark"></span><span>OAK HARBOR</span></div>
    <h1 class="holder-name">DORIAN KESTRUP</h1>
    <div class="divider divider--long"></div>
    <div class="divider divider--short"></div>
    <ul class="contact-list">
      <li class="contact-item">
        <svg class="contact-icon" viewBox="0 0 24 24" aria-hidden="true"><path fill="currentColor" d="M6.6 10.8c1.4 2.8 3.8 5.1 6.6 6.6l2.2-2.2c.3-.3.7-.4 1-.2 1.1.4 2.3.6 3.6.6.6 0 1 .4 1 1V20c0 .6-.4 1-1 1C10.6 21 3 13.4 3 4c0-.6.4-1 1-1h3.5c.6 0 1 .4 1 1 0 1.3.2 2.5.6 3.6.1.3 0 .7-.2 1z"/></svg>
        <span>800-555-0147</span>
      </li>
      <li class="contact-item">
        <svg class="contact-icon" viewBox="0 0 24 24" aria-hidden="true"><path fill="currentColor" d="M2 5h20v14H2z"/><path fill="none" stroke="#fff" stroke-width="1.6" d="M2.5 5.5 12 13l9.5-7.5M2.5 18.5l7-6.5m12 6.5-7-6.5"/></svg>
        <span>dorian@oakharbor-legal.com</span>
      </li>
      <li class="contact-item">
        <svg class="contact-icon" viewBox="0 0 24 24" aria-hidden="true"><g fill="none" stroke="currentColor" stroke-width="1.8"><circle cx="12" cy="12" r="9.5"/><ellipse cx="12" cy="12" rx="4" ry="9.5"/><path d="M2.5 12h19M4 7h16M4 17h16"/></g></svg>
        <span>www.oakharbor-legal.com</span>
      </li>
    </ul>
  </section>

  <section class="card card--back" aria-label="Business card back">
    <div class="back-brand"><span class="brand-mark"></span><span>OAK HARBOR</span></div>
  </section>
</main>
</body>
</html>
```